Personal Business Card Design Project

I require a two sided personal business card design.

I am a 35 year old Angel Investor and I invest in various niche internet and F&B projects in China. I am Chinese Australian

One side should be in English and the other side should be in Chinese.

My English details are:

Milo Varden
Angel Investor

China: +86 1703 482 5164
Hong Kong: +852 6437 2189
Email: milo@mvardenmail.com
Address: Flat 2407, Block 6, Birchmoor Terrace,
52 Qiaolan Road (near Fengyu Road),
Shanghai, 200417,
China

My Chinese details are (do not print the text in brackets)

韦朗舟 (Name)
天使投资者(Angel Investor)

中国 (China): +86 1703 482 5164
香港 (Hong Kong): +852 6437 2189
Email: milo@mvardenmail.com
地址 (Address): 上海市桥澜路52号6号楼2407室
枫影华苑, 中国 200417

Target Market(s)

I will only give this card to present to new partners and suppliers and people asking for funding. Not customers.

Industry/Entity Type

Internet

Requirements
Must have
• Something a little humourous in terms of graphics that suggest helping something to grow since I invest in startups. But I want a sophisticated look to it as well.
Nice to have
• Black and White tongue in cheek graphics but not overboard.

The whole card can be not conventional in shape or have cutouts but still retain the business standard business card size.

```html
<!DOCTYPE html>
<html lang="en">
<head>
<meta charset="utf-8">
<title>Milo Varden — Business Card</title>
<link rel="stylesheet" href="https://fonts.googleapis.com/css2?family=Crimson+Text:wght@400;600;700&family=Noto+Sans+SC:wght@400;500&display=swap">
<style>
  :root {
    --backdrop: #dcdcdc;
    --card-light: #ffffff;
    --card-dark: #3b3b3b;
    --ink-dark: #2a2a2a;
    --ink-light: #f2f2f2;
    --wing-light: #b9b9b9;
    --wing-dark: #8a8a8a;
  }
  * { margin: 0; padding: 0; box-sizing: border-box; }
  html, body { width: 900px; height: 1200px; overflow: hidden; }
  body {
    background: var(--backdrop);
    position: relative;
    font-family: "Crimson Text", Georgia, serif;
  }
  .card {
    position: absolute;
    left: 66px;
    width: 756px;
    height: 432px;
  }
  .card--english { top: 84px; background: var(--card-light); color: var(--ink-dark); }
  .card--chinese { top: 576px; background: var(--card-dark); color: var(--ink-light); font-family: "Crimson Text", "Noto Sans SC", serif; }

  .wing {
    position: absolute;
    border-radius: 60% 10% 70% 40% / 70% 20% 60% 40%;
  }
  .card--english .wing {
    left: 534px; top: 48px; width: 186px; height: 96px;
    background: linear-gradient(160deg, rgba(185,185,185,0.9), rgba(225,225,225,0.4));
  }
  .card--chinese .wing {
    left: 528px; top: 40px; width: 168px; height: 78px;
    background: linear-gradient(160deg, rgba(150,150,150,0.9), rgba(90,90,90,0.4));
  }

  .name {
    position: absolute; left: 42px; top: 36px;
    font-weight: 700; font-size: 31px; letter-spacing: 0.22em; line-height: 1;
  }
  .title {
    position: absolute; left: 42px; top: 72px;
    font-size: 28px; letter-spacing: 0.2em; line-height: 1;
  }
  .contact {
    position: absolute; left: 42px; top: 166px;
    font-size: 24px; line-height: 28px;
  }
  .address {
    position: absolute; left: 42px; top: 262px;
    font-size: 24px; line-height: 28px;
  }

  .card--chinese .name {
    font-family: "Noto Sans SC", sans-serif; font-weight: 500;
    font-size: 36px; letter-spacing: 0.02em; top: 42px;
  }
  .card--chinese .title {
    font-family: "Noto Sans SC", sans-serif; font-size: 27px;
    letter-spacing: 0.08em; top: 88px;
  }
  .card--chinese .contact { top: 180px; line-height: 30px; font-family: "Crimson Text", "Noto Sans SC", serif; }
  .card--chinese .address { top: 306px; line-height: 30px; font-family: "Crimson Text", "Noto Sans SC", serif; }
</style>
</head>
<body>
  <section class="card card--english">
    <div class="wing" role="img" aria-label="Soft grey feathered wing illustration"></div>
    <h1 class="name">MILO VARDEN</h1>
    <p class="title">ANGEL INVESTOR</p>
    <div class="contact">
      <p>China: +86 1703 482 5164</p>
      <p>Hong Kong: +852 6437 2189</p>
      <p>Email: milo@mvardenmail.com</p>
    </div>
    <div class="address">
      <p>Address: Flat 2407, Block 6, Birchmoor Terrace</p>
      <p>52 Qiaolan Road (near Fengyu Road)</p>
      <p>Shanghai, 200417</p>
      <p>China</p>
    </div>
  </section>

  <section class="card card--chinese" lang="zh">
    <div class="wing" role="img" aria-label="Soft grey feathered wing illustration"></div>
    <h2 class="name">韦朗舟</h2>
    <p class="title">天使投资者</p>
    <div class="contact">
      <p>中国: +86 1703 482 5164</p>
      <p>香港: +852 6437 2189</p>
      <p>Email: milo@mvardenmail.com</p>
    </div>
    <div class="address">
      <p>地址: 上海市桥澜路52号6号楼2407室</p>
      <p>枫影华苑, 中国 200417</p>
    </div>
  </section>
</body>
</html>
```